BrambleWorks business card

Looking for business card design that supports our company/software values. We have 2 logo designs at the moment but open to change if you think you can enhance the brand. Check out website www.brambleworks.com.au.

Target Market(s)

Education

Contact Information for Business Card

Name, title, mobile, email and website

Font styles to use
Sans Serif

Colors

Designer to choose colors to be used in the design.

Requirements
Must have
• BrambleWorks logo with tree and tagline on rear side with dark grey background colour

```html
<!DOCTYPE html>
<html lang="en">
<head>
<meta charset="utf-8">
<title>BrambleWorks business card</title>
<link href="https://fonts.googleapis.com/css2?family=Open+Sans:wght@400;600;700&family=Ubuntu:wght@400&display=swap" rel="stylesheet">
<style>
  :root {
    --backdrop: #808185;
    --amber: #fbb935;
    --charcoal: #3a3a3c;
    --white: #ffffff;
    --ink: #3d3d3f;
  }
  html, body {
    margin: 0;
    padding: 0;
    width: 1200px;
    height: 848px;
    overflow: hidden;
    background: var(--backdrop);
  }
  .canvas {
    position: relative;
    width: 1200px;
    height: 848px;
  }
  .card {
    position: absolute;
    left: 437px;
    width: 344px;
    height: 223px;
    border-radius: 31px;
    overflow: hidden;
  }
  .card--front { top: 167px; }
  .card--back { top: 495px; }
  .card svg { display: block; width: 100%; height: 100%; }
  .brand-name { font-family: "Ubuntu", sans-serif; font-weight: 400; }
  .brand-tagline { font-family: "Ubuntu", sans-serif; font-weight: 400; }
  .holder-name { font-family: "Open Sans", sans-serif; font-weight: 700; }
  .holder-title { font-family: "Open Sans", sans-serif; font-weight: 600; letter-spacing: 5px; }
  .contact-text { font-family: "Open Sans", sans-serif; font-weight: 600; }
</style>
</head>
<body>
<main class="canvas">

  <section class="card card--front" aria-label="Card front">
    <svg viewBox="0 0 503 326" xmlns="http://www.w3.org/2000/svg">
      <rect class="card-face" width="503" height="326" fill="var(--amber)"/>
      <path class="divider-band" d="M0,126 C170,118 310,160 336,326 L0,326 Z" fill="var(--white)"/>
      <path class="dark-field" d="M0,140 C160,134 292,176 322,326 L0,326 Z" fill="var(--charcoal)"/>
      <g class="brand-lockup">
        <circle class="brand-dot" cx="168" cy="76" r="26" fill="var(--ink)"/>
        <text class="brand-name" x="221" y="78" font-size="38" fill="var(--ink)">BrambleWorks</text>
        <line class="brand-rule" x1="222" y1="87" x2="408" y2="87" stroke="var(--ink)" stroke-width="1.2"/>
        <text class="brand-tagline" x="226" y="105" font-size="15" fill="var(--ink)">Student Success Platform</text>
      </g>
    </svg>
  </section>

  <section class="card card--back" aria-label="Card back">
    <svg viewBox="0 0 503 326" xmlns="http://www.w3.org/2000/svg">
      <rect class="card-face" width="503" height="326" fill="var(--charcoal)"/>
      <path class="accent-band" d="M0,126 C170,120 272,170 300,326 L0,326 Z" fill="var(--amber)"/>
      <path class="light-field" d="M0,141 C160,138 252,180 286,326 L0,326 Z" fill="var(--white)"/>

      <text class="holder-name" x="251" y="75" font-size="33" fill="var(--white)" text-anchor="middle">MARTIN KELLER</text>
      <text class="holder-title" x="253" y="98" font-size="16" fill="var(--white)" text-anchor="middle">DIRECTOR</text>

      <g class="contact-list">
        <g class="contact contact--mobile">
          <circle cx="292" cy="216" r="11" fill="var(--white)"/>
          <rect x="288" y="209" width="8" height="14" rx="1.5" fill="none" stroke="var(--charcoal)" stroke-width="1.3"/>
          <text class="contact-text" x="308" y="220" font-size="11" fill="var(--white)">+39 612 480 3371</text>
        </g>
        <g class="contact contact--phone">
          <circle cx="313" cy="250" r="11" fill="var(--white)"/>
          <path d="M306,248 Q313,242 320,248 L318,251 L315,249 L311,249 L308,251 Z" fill="var(--charcoal)"/>
          <rect x="308" y="251" width="10" height="5" rx="1" fill="var(--charcoal)"/>
          <text class="contact-text" x="329" y="254" font-size="11" fill="var(--white)">+39 634 215 9087</text>
        </g>
        <g class="contact contact--email">
          <circle cx="326" cy="283" r="11" fill="var(--white)"/>
          <rect x="320" y="279" width="12" height="8" fill="var(--charcoal)"/>
          <path d="M320,279 L326,284 L332,279" fill="none" stroke="var(--white)" stroke-width="1"/>
          <text class="contact-text" x="342" y="287" font-size="11" fill="var(--white)">keller@brambleworks.com</text>
        </g>
      </g>

      <g class="brand-lockup">
        <circle class="brand-dot" cx="72" cy="276" r="20" fill="var(--ink)"/>
        <text class="brand-name" x="104" y="277" font-size="24" fill="var(--ink)">BrambleWorks</text>
        <line class="brand-rule" x1="105" y1="283" x2="228" y2="283" stroke="var(--ink)" stroke-width="0.8"/>
        <text class="brand-tagline" x="110" y="294" font-size="9.5" fill="var(--ink)">Student Success Platform</text>
      </g>
    </svg>
  </section>

</main>
</body>
</html>
```